Business Cards for Marco and Tobin

Design of business cards for two people with the recently created brand Valcor Mobile. Valcor Mobile wants to become a worldwide major player on the secondhand phone market. It gathers send hand phones from individuals, refurbish them and sell them throughout the world. It has a green impact (recycling) and we also contribute to social project in Africa (a percentage of our benefits are sent to build school, sport facilities, etc.

Target Market(s)

B2B - Marco and Tobin are in contact with distributors across Africa.

Industry/Entity Type

Wireless Communication

Contact Information for Business Card

Marco Feuillet
Head of Emerging Markets
Valcor Energy South Africa (Pty) Ltd
Kestrel Road 47
2031 Sandton - Johannesburg
South Africa
Tel: + 27 10 555 0148
Mobile : +27 82 55 104
Email : marco.feuillet@valcormobile.example
Skype: marco.feuillet
Web: www.valcormobile.example
 

Tobin Farrow
Head of Southern Africa
Kestrel Road 47
South Africa
Tel: + 27 10 555 0148
Mobile: +27 83 555 0276
Email: tobin.farrow@valcormobile.example
Skype: tobin.farrow
Web: www.valcormobile.example

Requirements
Must have
• The cards need to be "serious", trustable, with a worldwide presence.
Nice to have
• Some "green" / recycling touch would be nice but not necessary if in contradiction with the general design.

```html
<!DOCTYPE html>
<html lang="en">
<head>
<meta charset="utf-8">
<title>Valcor Mobile – Business Card</title>
<link rel="stylesheet" href="https://fonts.googleapis.com/css2?family=Arimo:wght@400;700&display=swap">
<style>
  :root {
    --backdrop: #e9e9ec;
    --paper: #ffffff;
    --navy: #0b2d45;
    --brand-blue: #2f8fd8;
    --ink: #1d3c57;
    --grey-text: #555c63;
    --rule: #c9cdd1;
  }
  * { box-sizing: border-box; margin: 0; padding: 0; }
  html, body {
    width: 1200px; height: 800px; overflow: hidden;
    background: var(--backdrop);
    font-family: "Arimo", Arial, sans-serif;
  }
  .sheet {
    width: 1200px; height: 800px;
    display: flex; align-items: center; justify-content: center; gap: 48px;
  }
  .card {
    width: 540px; height: 318px; position: relative;
    box-shadow: 0 2px 10px rgba(0,0,0,0.08);
  }
  /* Front */
  .card-front { background: var(--paper); }
  .brand-lockup {
    position: absolute; left: 34px; top: 40px;
    display: flex; align-items: center; gap: 10px;
  }
  .brand-dot { width: 22px; height: 22px; border-radius: 50%; background: var(--brand-blue); }
  .brand-name { font-size: 24px; font-weight: 700; color: var(--brand-blue); }
  .person {
    position: absolute; right: 34px; top: 40px; text-align: left; width: 220px;
  }
  .person-name { font-size: 19px; color: var(--ink); letter-spacing: 0.3px; }
  .person-name strong { font-weight: 700; }
  .person-title { font-size: 13px; color: var(--grey-text); margin-top: 4px; }
  .person-chat { font-size: 12px; color: var(--grey-text); margin-top: 5px; display: flex; align-items: center; gap: 6px; }
  .chat-dot { width: 12px; height: 12px; border-radius: 50%; background: var(--brand-blue); }
  .company {
    position: absolute; left: 34px; top: 148px;
    font-size: 15px; color: var(--brand-blue);
  }
  .rule {
    position: absolute; left: 34px; right: 34px; top: 172px;
    border-top: 1px solid var(--rule);
  }
  .address {
    position: absolute; left: 34px; top: 182px;
    font-size: 12px; color: var(--grey-text);
  }
  .contact-row {
    position: absolute; left: 34px; right: 34px; top: 210px;
    display: flex; gap: 60px;
  }
  .contact-group { display: flex; gap: 8px; font-size: 12px; color: var(--grey-text); line-height: 1.45; }
  .contact-icon { width: 14px; height: 14px; margin-top: 2px; flex: none; }
  /* Back */
  .card-back {
    background: var(--navy);
    display: flex; align-items: center; justify-content: center; gap: 10px;
  }
  .card-back .brand-name { font-size: 30px; }
  .card-back .brand-dot { width: 26px; height: 26px; }
</style>
</head>
<body>
<main class="sheet">
  <section class="card card-front" aria-label="Business card front">
    <div class="brand-lockup">
      <span class="brand-dot"></span>
      <span class="brand-name">Valcor Mobile</span>
    </div>
    <div class="person">
      <p class="person-name"><strong>MARCO</strong> FEUILLET</p>
      <p class="person-title">Head of Emerging Markets</p>
      <p class="person-chat"><span class="chat-dot"></span>marco.feuillet</p>
    </div>
    <p class="company">Valcor Energy South Africa (Pty) Ltd</p>
    <div class="rule"></div>
    <p class="address">Kestrel Road 47, 2031 Sandton - Johannesburg, South Africa</p>
    <div class="contact-row">
      <div class="contact-group">
        <svg class="contact-icon" viewBox="0 0 24 24" aria-hidden="true">
          <path fill="#1d3c57" d="M6.6 10.8a15 15 0 0 0 6.6 6.6l2.2-2.2c.3-.3.7-.4 1-.2 1.1.4 2.3.6 3.6.6.6 0 1 .4 1 1V20c0 .6-.4 1-1 1C10.6 21 3 13.4 3 4c0-.6.4-1 1-1h3.5c.6 0 1 .4 1 1 0 1.3.2 2.5.6 3.6.1.3 0 .7-.2 1z"/>
        </svg>
        <div>+ 27 10 555 0148<br>+27 82 55 104</div>
      </div>
      <div class="contact-group">
        <svg class="contact-icon" viewBox="0 0 24 24" aria-hidden="true" fill="none" stroke="#1d3c57" stroke-width="2">
          <circle cx="12" cy="12" r="9"/><path d="M3 12h18M12 3c3 3 3 15 0 18M12 3c-3 3-3 15 0 18"/>
        </svg>
        <div>marco.feuillet@valcormobile.example<br>www.valcormobile.example</div>
      </div>
    </div>
  </section>
  <section class="card card-back" aria-label="Business card back">
    <span class="brand-dot"></span>
    <span class="brand-name">Valcor Mobile</span>
  </section>
</main>
</body>
</html>
```